Psychologist website

Simple psychologist website
Site map:
home
self-test
common conditions
children
contact
about
info

Current website:
http://www.corvalepsychology.com.au/

Not in love with logo, or colours etc - open brief
Happy for new font/style/logo for company name

Customer wants clean, credible and warm and friendly look & feel
stock photos OK

Brief:

One home page - simple with 2 or 3 small areas to tease and attract the user and one template page to suit all the other pages

Pages structurally similar to
http://www.wendlecourt.com.au/
In that the home page is different and the other pages are based on one template

Requirements
Must have
• 2 pages - one home page and one template page
• navigation for site map

```html
<!DOCTYPE html>
<html lang="en">
<head>
<meta charset="utf-8">
<title>Corvalepsychology</title>
<link rel="stylesheet" href="https://fonts.googleapis.com/css2?family=Arimo:wght@400;700&family=Gelasio:ital@1&family=Tinos&display=swap">
<style>
:root{
  --page:#ffffff;
  --panel:#dddddd;
  --ink:#555555;
  --nav-ink:#444444;
  --brand:#9a9a9a;
  --green:#5cb531;
  --green-dark:#2f8a12;
  --link-ink:#5c5600;
  --arrow:#cc2200;
  --divider:#b9b9b9;
  --hero-a:#eef4e6;
  --hero-b:#f3c8d6;
  --hero-c:#cbe8f6;
}
*{box-sizing:border-box;margin:0;padding:0}
html,body{width:1200px;height:1000px;overflow:hidden;background:var(--page)}
.canvas{position:relative;width:1200px;height:1000px}
.brand-name{position:absolute;left:110px;top:180px;font:700 42px/1 "Arimo",sans-serif;color:var(--brand);letter-spacing:1.5px}
.hero-art{position:absolute;left:655px;top:75px;width:450px;height:280px;
  background:linear-gradient(180deg,var(--hero-a) 0%,var(--hero-b) 50%,var(--hero-c) 100%)}
.main-nav{position:absolute;left:104px;top:362px;width:984px;height:42px;display:flex;
  background:linear-gradient(#ffffff,#ececec 70%,#d8d8d8);border-radius:0 0 6px 6px;box-shadow:0 2px 2px rgba(0,0,0,.25)}
.main-nav a{font:700 14px/38px "Arimo",sans-serif;color:var(--nav-ink);text-decoration:none;padding-left:11px;border-right:1px solid var(--divider);width:126px}
.main-nav a:nth-child(6){width:127px}
.main-nav a:last-child{border-right:0;flex:1;padding-left:20px}
.teaser{position:absolute;background:var(--panel)}
.teaser-title{position:absolute;height:22px;background:var(--green);color:#fff;font:700 18px/22px "Arimo",sans-serif;text-align:center}
.teaser-text{position:absolute;font:italic 16px/19.2px "Gelasio",serif;color:var(--ink)}
.learn-more{position:absolute;width:110px;height:31px;border-radius:8px;background:linear-gradient(#7fd04a,var(--green-dark));
  border:1px solid #1f6a08;color:#fff;font:400 13px/29px "Arimo",sans-serif;text-align:center;text-decoration:none;letter-spacing:.3px}
.services{left:98px;top:429px;width:306px;height:339px}
.about{left:438px;top:429px;width:295px;height:328px}
.link-panel{position:absolute;left:767px;top:425px;width:322px;height:349px;background:var(--panel);border-radius:8px;overflow:hidden}
.link-row{position:absolute;left:0;width:322px;height:38.5px;border-top:1px solid #fff}
.link-row svg{position:absolute;left:0;top:0}
.link-row span{position:absolute;left:56px;top:2px;font:700 14px/1 "Arimo",sans-serif;color:var(--link-ink)}
.rule{position:absolute;left:98px;top:795px;width:635px;border-top:1px dotted #999}
.intro{position:absolute;left:98px;top:807px;width:622px;font:15px/19px "Tinos",serif;color:var(--ink);word-spacing:.8px}
.site-footer{position:absolute;left:87px;top:953px;width:1020px;height:47px;background:var(--panel)}
.site-footer a{position:absolute;left:11px;top:14px;font:17px/1 "Tinos",serif;color:var(--nav-ink)}
</style>
</head>
<body>
<div class="canvas">
  <div class="brand-name">Corvalepsychology</div>
  <div class="hero-art" role="img" aria-label="Header illustration about levels of human needs"></div>

  <nav class="main-nav">
    <a href="#">Home</a><a href="#">Self-Test</a><a href="#">About</a><a href="#">Children</a><a href="#">Info</a><a href="#">Contact</a><a href="#">common conditions</a>
  </nav>

  <section class="teaser services">
    <h2 class="teaser-title" style="left:6px;top:11px;width:294px">Our Services</h2>
    <p class="teaser-text" style="left:6px;top:40px;width:294px">lumivora.com, based in India, offers all type design and web solutions.Our experience since 2010, we continue to provide our clients with the latest in website technology, development, and web design while offering functional, fast-loading, and visitor-friendly websites also provide logo design,wedding photography, wedding degital album making,fine arts and more.We can capture your vision and ideas and transform them into an effective design that is uniqu</p>
    <a class="learn-more" href="#" style="left:189px;top:298px">LEARN MORE</a>
  </section>

  <section class="teaser about">
    <h2 class="teaser-title" style="left:0;top:6px;width:295px">About Us</h2>
    <p class="teaser-text" style="left:0;top:35px;width:290px">lumivora.com, based in India, offers all type design and web solutions.Our experience since 2010, we continue to provide our clients with the latest in website technology, development, and web design while offering functional, fast-loading, and visitor-friendly websites also provide logo design,wedding photography, wedding degital album making,fine arts and more.We can capture your vision and ideas and transform them into an effective design that is uniqu</p>
    <a class="learn-more" href="#" style="left:183px;top:292px">LEARN MORE</a>
  </section>

  <aside class="link-panel">
    <div class="link-row" style="top:40px"><svg width="322" height="38"><path d="M180 0 Q260 16 322 2 L322 10 Q250 24 180 0Z" fill="#fff"/><path d="M8 10 L17 15.5 L8 21Z" fill="var(--arrow)"/></svg><span>Your Link1</span></div>
    <div class="link-row" style="top:78.5px"><svg width="322" height="38"><path d="M180 0 Q260 16 322 2 L322 10 Q250 24 180 0Z" fill="#fff"/><path d="M8 10 L17 15.5 L8 21Z" fill="var(--arrow)"/></svg><span>Your Link2</span></div>
    <div class="link-row" style="top:117px"><svg width="322" height="38"><path d="M180 0 Q260 16 322 2 L322 10 Q250 24 180 0Z" fill="#fff"/><path d="M8 10 L17 15.5 L8 21Z" fill="var(--arrow)"/></svg><span>Your Link3</span></div>
    <div class="link-row" style="top:155.5px"><svg width="322" height="38"><path d="M180 0 Q260 16 322 2 L322 10 Q250 24 180 0Z" fill="#fff"/><path d="M8 10 L17 15.5 L8 21Z" fill="var(--arrow)"/></svg><span>Your Link4</span></div>
    <div class="link-row" style="top:194px"><svg width="322" height="38"><path d="M180 0 Q260 16 322 2 L322 10 Q250 24 180 0Z" fill="#fff"/><path d="M8 10 L17 15.5 L8 21Z" fill="var(--arrow)"/></svg><span>Your Link5</span></div>
    <div class="link-row" style="top:232.5px"><svg width="322" height="38"><path d="M180 0 Q260 16 322 2 L322 10 Q250 24 180 0Z" fill="#fff"/><path d="M8 10 L17 15.5 L8 21Z" fill="var(--arrow)"/></svg><span>Your Link6</span></div>
    <div class="link-row" style="top:271px"><svg width="322" height="38"><path d="M180 0 Q260 16 322 2 L322 10 Q250 24 180 0Z" fill="#fff"/><path d="M8 10 L17 15.5 L8 21Z" fill="var(--arrow)"/></svg><span>Your Linl7</span></div>
    <div class="link-row" style="top:309.5px;height:40px"></div>
  </aside>

  <div class="rule"></div>
  <p class="intro">lumivora.com, based in India, offers all type design and web solutions.Our experience since 2010, we continue to provide our clients with the latest in website technology, development, and web design while offering functional, fast-loading, and visitor-friendly websites also provide logo design,wedding photography, wedding degital album making,fine arts and more.We can capture your vision and ideas and transform them into an effective design that is uniquely your own. We can produce design for you that is both modern and adaptable</p>

  <footer class="site-footer"><a href="#">Copy right@www.brightmesa.us</a></footer>
</div>
</body>
</html>
```